Business Card Design Project

We need a business card design for a management consultancy focused on financial innovation and digital money, run by experts from the Financial Services, Telecoms and Money Transfer industries.
Our products include services such as Mobile Payments, Mobile Money, Digital Wallets, Online Payments, Branchless Banking and more. We work with regulatory information, business plans, financial modelling, strategic planning, new products functional specification, new technologies evaluation, etc.
See company logo attached.
We would like to see 2 versions: one in portuguese and one in english (regarding data information). You can see below information needed (whenever there is a difference between the two versions, the first one is in english and the second one in portuguese).

Name
Position
Phone/ Tel: ++55-11-xxxx-xxxx
Cell/ Cel: ++55-11-9 xxxx-xxxx
Dr. Tavares Lobato Av., 318 - Tower II - 16th floor / Avenida Dr. Tavares Lobato, 318 - Torre II - 16o. andar
São Paulo - SP
01327-118 - Brazil/ 01327-118 - Brasil

Target Market(s)

Audience: C-level executives from banks, credit card companies, acquirers, IT developers, retailers

Industry/Entity Type

Financial

Requirements
Must have
• Must use the logo and information above. Front must have white background. Back side should have only logo.
Nice to have
• Back should be in another colour but if it seems too exxagerated, maintain back in white also.
Should not have
• Do not add other illustrations to the business card.

```html
<!DOCTYPE html>
<html lang="en">
<head>
<meta charset="utf-8">
<title>R Halvorsen Management Consulting – Business Cards</title>
<link rel="stylesheet" href="https://fonts.googleapis.com/css2?family=Cinzel:wght@400&family=Open+Sans:wght@400;600&display=swap">
<style>
  :root {
    --backdrop: #e9e6e1;
    --card: #ffffff;
    --navy: #1f2a5c;
    --ink: #1b1b1b;
    --mark: #c9c9c9;
    --shadow: rgba(0, 0, 0, 0.22);
  }
  * { box-sizing: border-box; margin: 0; padding: 0; }
  html, body {
    width: 1200px;
    height: 1023px;
    overflow: hidden;
    background: var(--backdrop);
  }
  .sheet {
    position: relative;
    width: 1200px;
    height: 1023px;
  }
  .card {
    position: absolute;
    width: 640px;
    height: 366px;
    background: var(--card);
    box-shadow: 0 10px 28px var(--shadow);
  }
  .card--back { left: 120px; top: 70px; }
  .card--front { left: 440px; top: 560px; }

  .brand {
    position: absolute;
    display: flex;
    align-items: center;
    gap: 12px;
  }
  .brand__square {
    width: 22px;
    height: 22px;
    background: var(--mark);
    flex: none;
  }
  .brand__name {
    font-family: "Open Sans", sans-serif;
    font-weight: 400;
    font-size: 18px;
    line-height: 1;
    color: var(--ink);
    white-space: nowrap;
  }
  .card--back .brand { right: 56px; bottom: 80px; }
  .card--front .brand { right: 44px; bottom: 44px; }

  .holder {
    position: absolute;
    left: 48px;
    top: 44px;
  }
  .holder__name {
    font-family: "Cinzel", serif;
    font-weight: 400;
    font-size: 30px;
    color: var(--navy);
    letter-spacing: 1px;
  }
  .holder__role {
    font-family: "Open Sans", sans-serif;
    font-size: 14px;
    color: var(--ink);
    margin-top: 2px;
  }
  .contact {
    list-style: none;
    margin-top: 24px;
    font-family: "Open Sans", sans-serif;
    font-size: 16px;
    color: var(--ink);
  }
  .contact li {
    display: flex;
    align-items: center;
    gap: 10px;
    line-height: 26px;
  }
  .contact svg { width: 16px; height: 16px; flex: none; }
  .address {
    font-style: normal;
    margin-top: 20px;
    font-family: "Open Sans", sans-serif;
    font-size: 15px;
    line-height: 23px;
    color: var(--ink);
  }
</style>
</head>
<body>
<main class="sheet">
  <section class="card card--back" aria-label="Card back">
    <div class="brand">
      <div class="brand__square"></div>
      <p class="brand__name">R Halvorsen Management Consulting</p>
    </div>
  </section>

  <section class="card card--front" aria-label="Card front">
    <div class="holder">
      <h1 class="holder__name">DANIEL MOREIRA</h1>
      <p class="holder__role">General Manager</p>
      <ul class="contact">
        <li>
          <svg viewBox="0 0 16 16" aria-hidden="true"><path fill="#1f2a5c" d="M3 2h3l1.2 3-1.7 1.2a8 8 0 0 0 4.3 4.3L11 8.8 14 10v3a1 1 0 0 1-1 1C7 14 2 9 2 3a1 1 0 0 1 1-1z"/></svg>
          +55-11-987-654
        </li>
        <li>
          <svg viewBox="0 0 16 16" aria-hidden="true"><rect x="4" y="1" width="8" height="14" rx="1.5" fill="#1f2a5c"/><rect x="5.5" y="3" width="5" height="7" fill="#fff"/><circle cx="8" cy="12.5" r="0.9" fill="#fff"/></svg>
          +55-11-9-987-654
        </li>
      </ul>
      <address class="address">
        Dr. Tavares Lobato Av.,<br>
        318 - Tower II - 16th floor<br>
        São Paulo<br>
        01327-118 - Brazil
      </address>
    </div>
    <div class="brand">
      <div class="brand__square"></div>
      <p class="brand__name">R Halvorsen Management Consulting</p>
    </div>
  </section>
</main>
</body>
</html>
```